Newsletter Design Project

Hi there! I am an sketch artist/educator in the wedding space and need a few newsletter templates that someone on my team can easily drop in text and photos, but look clean, high end, and that can represent my brand well.
Updates

Reason: We have edits out to a designer and waiting for the design to come back.

Target Market(s)

High end - luxury (but approachable) wedding planners

Industry/Entity Type

Wedding

Font styles to use
Serif

Colors

Designer to choose colors to be used in the design.

Requirements
Must have
• Easy templates that can be dropped into mailchimp and where we can drop in text/photos very easily. Clean layout design. I think I'm looking for something white and gray - since all my images will have the color. But will leave it up to the designers.
Should not have
• nothing over the top or fancy.

```html
<!DOCTYPE html>
<html lang="en">
<head>
<meta charset="utf-8">
<title>Wren Atelier Newsletter</title>
<link href="https://fonts.googleapis.com/css2?family=Arimo:wght@400;700&family=Libre+Baskerville:ital,wght@0,400;0,700;1,400&display=swap" rel="stylesheet">
<style>
  :root {
    --page: #ffffff;
    --ink: #4d4d4d;
    --ink-soft: #8a8a8a;
    --blush: #fbe0d9;
    --blush-deep: #f4b8aa;
    --rule: #e6e6e6;
    --black: #1a1a1a;
  }
  * { box-sizing: border-box; margin: 0; padding: 0; }
  html, body { width: 1200px; height: 1200px; overflow: hidden; background: var(--page); }
  body { font-family: "Arimo", Arial, sans-serif; color: var(--ink); }

  .newsletter {
    width: 1200px; height: 1200px;
    display: flex; justify-content: center; gap: 80px;
    padding: 40px 60px;
  }
  .column { width: 480px; display: flex; flex-direction: column; align-items: center; }

  .masthead { text-align: center; margin-bottom: 22px; }
  .brand-name {
    font-family: "Libre Baskerville", Georgia, serif; font-weight: 400;
    font-size: 38px; color: var(--black); letter-spacing: 1px;
    margin-bottom: 26px;
  }
  .tagline {
    font-family: "Libre Baskerville", Georgia, serif; font-style: italic;
    font-size: 15px; color: var(--ink-soft); margin-bottom: 6px;
  }
  .headline { font-size: 28px; font-weight: 700; color: var(--ink); }

  .offer { width: 100%; display: flex; flex-direction: column; align-items: center; margin-bottom: 18px; }
  .offer-photo { width: 210px; height: 210px; border-radius: 50%; }
  .photo-warm { background: radial-gradient(circle at 40% 40%, #f36fb8 0%, #f9a05a 40%, #fbd34d 70%, #fde6ec 100%); }
  .photo-cool { background: radial-gradient(circle at 55% 60%, #3f8fd0 0%, #7fd1c7 35%, #b6e08a 60%, #f2f8fa 88%); }
  .eyebrow {
    font-family: "Libre Baskerville", Georgia, serif; font-style: italic;
    font-size: 12px; color: var(--blush-deep); margin-top: 8px;
  }
  .offer-title { font-size: 13px; font-weight: 700; text-transform: uppercase; color: var(--ink); margin-top: 2px; }
  .button {
    display: block; text-align: center; text-decoration: none;
    background: var(--blush); color: var(--ink); font-weight: 700;
    border-radius: 20px; font-size: 12px; padding: 8px 0; margin-top: 10px;
  }
  .offer .button { width: 100%; }

  .artist { width: 100%; display: flex; gap: 20px; padding-bottom: 24px; border-bottom: 1px solid var(--rule); }
  .artist-text { flex: 1; }
  .artist-title {
    font-family: "Libre Baskerville", Georgia, serif; font-style: italic; font-weight: 400;
    font-size: 22px; color: var(--blush-deep); margin-bottom: 10px;
  }
  .artist-bio { font-size: 13px; line-height: 1.6; text-align: justify; color: var(--ink); }
  .artist .button { width: 110px; margin-top: 14px; }
  .artist-photo { width: 140px; height: 170px; background: linear-gradient(160deg, #e9d2cf, #f4e6ea 60%, #d8c7c2); }

  .gallery {
    width: 100%; display: grid; grid-template-columns: 1fr 1fr; gap: 16px;
    padding: 24px 0; border-bottom: 1px solid var(--rule);
  }
  .gallery-item { height: 200px; }
  .g1 { background: linear-gradient(180deg, #fbf0b8, #eef3f2 60%, #fafafa); }
  .g2 { background: linear-gradient(180deg, #f4f4f4, #e2dcd6); }
  .g3 { background: linear-gradient(160deg, #f1f1f0, #e3e1de); }
  .g4 { background: linear-gradient(180deg, #e7f5e3, #b9df9c 50%, #fafafa); }

  .footer { width: 100%; text-align: center; padding-top: 22px; }
  .footer-mark { font-family: "Libre Baskerville", Georgia, serif; font-size: 24px; color: var(--black); }
  .social { display: flex; justify-content: center; gap: 12px; margin: 14px 0 18px; }
  .social a { display: block; width: 34px; height: 34px; }
  .copyright { font-family: "Libre Baskerville", Georgia, serif; font-style: italic; font-size: 12px; color: var(--black); margin-bottom: 10px; }
  .contact-label { font-family: "Libre Baskerville", Georgia, serif; font-weight: 700; font-size: 11px; color: var(--black); }
  .contact-email { font-family: "Libre Baskerville", Georgia, serif; font-size: 11px; color: var(--black); margin-bottom: 12px; }
  .preferences { font-family: "Libre Baskerville", Georgia, serif; font-size: 10px; line-height: 1.5; color: var(--ink); }
</style>
</head>
<body>
<main class="newsletter">
  <section class="column">
    <header class="masthead">
      <div class="brand-name">Wren Atelier</div>
      <p class="tagline">Live A Creatively Inspired Life</p>
      <h1 class="headline">We can help you.</h1>
    </header>

    <article class="offer">
      <div class="offer-photo photo-warm" role="img" aria-label="Photo of watercolor swatches in pink, orange and yellow"></div>
      <p class="eyebrow">Take a Class</p>
      <h2 class="offer-title">Design Summer Sessions</h2>
      <a class="button" href="#">View All Sessions</a>
    </article>

    <article class="offer">
      <div class="offer-photo photo-cool" role="img" aria-label="Photo of a paint palette with blue and green watercolor swatches"></div>
      <p class="eyebrow">Work With Us</p>
      <h2 class="offer-title">Custom Creative Projects</h2>
      <a class="button" href="#">Hire Us Now</a>
    </article>

    <article class="offer">
      <div class="offer-photo photo-cool" role="img" aria-label="Photo of a paint palette with blue and green watercolor swatches"></div>
      <p class="eyebrow">Work With Us</p>
      <h2 class="offer-title">Custom Creative Projects</h2>
      <a class="button" href="#">Hire Us Now</a>
    </article>
  </section>

  <section class="column">
    <article class="artist">
      <div class="artist-text">
        <h2 class="artist-title">The Artist</h2>
        <p class="artist-bio">Hi! I'm Clara Voss – founder and creator of Wren Atelier &amp; The Drawing Room Series. I've always known that I wanted to live a creatively inspired life. At an early age, I would sit and sketch for hours, focusing on the smallest details. My passion is connecting and inspiring other creatives through art + design (cont.)</p>
        <a class="button" href="#">Read More</a>
      </div>
      <div class="artist-photo" role="img" aria-label="Portrait photo of the artist"></div>
    </article>

    <div class="gallery">
      <div class="gallery-item g1" role="img" aria-label="Sketch of a café storefront with yellow awning"></div>
      <div class="gallery-item g2" role="img" aria-label="Photo of a pen beside a sketched wedding cake"></div>
      <div class="gallery-item g3" role="img" aria-label="Photo of pencils on a sketch in progress"></div>
      <div class="gallery-item g4" role="img" aria-label="Watercolor illustration of a garden arch with greenery"></div>
    </div>

    <footer class="footer">
      <div class="footer-mark">Wren</div>
      <nav class="social" aria-label="Social links">
        <a href="#" aria-label="Social profile one"><svg viewBox="0 0 34 34" width="34" height="34"><circle cx="17" cy="17" r="15.5" fill="none" stroke="#1a1a1a" stroke-width="2"/></svg></a>
        <a href="#" aria-label="Social profile two"><svg viewBox="0 0 34 34" width="34" height="34"><circle cx="17" cy="17" r="15.5" fill="none" stroke="#1a1a1a" stroke-width="2"/></svg></a>
        <a href="#" aria-label="Social profile three"><svg viewBox="0 0 34 34" width="34" height="34"><circle cx="17" cy="17" r="15.5" fill="none" stroke="#1a1a1a" stroke-width="2"/></svg></a>
        <a href="#" aria-label="Website link"><svg viewBox="0 0 34 34" width="34" height="34"><circle cx="17" cy="17" r="15.5" fill="none" stroke="#1a1a1a" stroke-width="2"/><g fill="none" stroke="#1a1a1a" stroke-width="2" stroke-linecap="round"><path d="M15 19l4-4"/><path d="M14 15.5l-2 2a3 3 0 0 0 4.2 4.2l2-2"/><path d="M20 18.5l2-2a3 3 0 0 0-4.2-4.2l-2 2"/></g></svg></a>
      </nav>
      <p class="copyright">Copyright © studio@wrenmail.com</p>
      <p class="contact-label">EMAIL US:</p>
      <p class="contact-email">HELLO@WRENATELIER.COM</p>
      <p class="preferences">Want to change how you receive these emails?<br>You can update your preferences or unsubscribe from this list.</p>
    </footer>
  </section>
</main>
</body>
</html>
```